Corvane Agribusiness Consulting needs a Website Design.

We need a website design for a new company based in UK. Corvane offers agribusiness consulting and farm design services to farmers, smallholders and the wider agribusiness industry to assist clients in adopting more sustainable and regenerative production, processing and marketing practices.
Services are offered face-to-face and on a remote platform.
Services are offered in the UK and overseas.
We would like to see designs that reflect the natural environment, business and sustainability. Desired colours; green, blue, grey. The final design should communicate professionalism in the rural economy.
The design should be able to be customized by the client to make future changes and additions.
Target Market(s)
Farmers, smallholders, and the agricultural industry in UK and overseas.
Industry/Entity Type
Agribusiness
Number of Pages Required
4 page

```html
<!DOCTYPE html>
<html lang="en">
<head>
<meta charset="utf-8">
<title>Corvane Agribusiness Consulting</title>
<link href="https://fonts.googleapis.com/css2?family=Questrial&family=Dancing+Script:wght@600&display=swap" rel="stylesheet">
<style>
:root{
  --blue:#0a8ccf;
  --blue-deep:#1a6fc0;
  --green:#9bc93a;
  --green-dark:#3d8a1e;
  --grey-dark:#464646;
  --grey-mid:#8a8a8a;
  --text-grey:#666;
  --white:#fff;
  --wheat-1:#e3a43e;
  --wheat-2:#b86f1c;
  --board-1:#c8922c;
  --board-2:#a8721c;
}
*{box-sizing:border-box;margin:0;padding:0}
html,body{width:708px;height:1200px;overflow:hidden;background:var(--white)}
body{font-family:"Questrial",sans-serif;color:var(--text-grey);position:relative}
.page{position:relative;width:708px;height:1200px;overflow:hidden}
.abs{position:absolute}

/* hero */
.hero-photo{left:0;top:0;width:708px;height:416px;
  background:linear-gradient(180deg,#f0c274 0%,var(--wheat-1) 35%,#c98529 70%,var(--wheat-2) 100%)}
.nav-band{left:0;top:28px;width:708px;height:48px;background:rgba(255,255,255,.45)}
.brand{left:64px;top:36px;font-size:24px;color:var(--green-dark);display:flex;align-items:center;gap:6px}
.brand-dot{width:10px;height:10px;border-radius:50%;background:var(--green)}
.nav{left:352px;top:41px;display:flex;align-items:center;font-size:12px;color:#222}
.nav a{color:#222;text-decoration:none}
.nav .active{width:71px;height:22px;border-radius:3px;background:linear-gradient(#4aa6f0,var(--blue-deep));color:var(--white);text-align:center;line-height:22px;margin-right:16px}
.nav .item{margin-right:18px}
.headline{font-size:35px;color:var(--white);text-shadow:1px 1px 3px rgba(0,0,0,.35);line-height:1}
.headline .accent{color:var(--blue-deep)}
.line-1{left:118px;top:224px}
.line-2{left:220px;top:270px}
.slider-dots{left:562px;top:360px;display:flex;gap:6px}
.slider-dots span{width:11px;height:11px;border-radius:50%;background:var(--white)}
.slider-dots span.on{background:var(--blue)}

/* about */
.about{left:58px;top:387px;width:598px;height:147px;background:var(--blue);box-shadow:0 3px 5px rgba(0,0,0,.35);color:var(--white);text-align:center}
.about h2{font-weight:400;font-size:15px;margin-top:57px}
.about p{font-size:7px;line-height:8.6px;width:500px;margin:10px auto 0}
.about-photo{left:294px;top:324px;width:112px;height:112px;border-radius:50%;border:3px solid #ddd;
  background:linear-gradient(180deg,#cfe2ee 0%,#9cc0db 45%,#3f7a2a 60%,#6fa83a 100%);box-shadow:0 2px 4px rgba(0,0,0,.3)}

/* services */
.card{width:176px;height:238px;top:570px;background:var(--green);box-shadow:0 2px 4px rgba(0,0,0,.3);text-align:center;color:var(--white)}
.card-photo{width:176px;height:146px}
.card h3{font-weight:400;font-size:8px;color:#333;margin-top:7px}
.card hr{border:0;border-top:1px solid #6f9a2a;width:126px;margin:4px auto 5px}
.card p{font-size:6.6px;line-height:8.4px;width:132px;margin:0 auto}
.card .btn{display:inline-block;margin-top:9px;width:60px;height:14px;border-radius:7px;background:var(--blue);border:1px solid var(--white);font-size:7.5px;line-height:12px;color:var(--white)}
.c1{left:58px}.c2{left:270px}.c3{left:480px}
.p1{background:linear-gradient(180deg,#3a7a1c,#8cc440 60%,#2f5f16)}
.p2{background:linear-gradient(180deg,#3b7fcf 0%,#9fc8ea 45%,#6a9a3a 62%,#c9c1b2 100%)}
.p3{background:linear-gradient(135deg,#5d8a2a,#d9482a 40%,#e98a2e 65%,#ece5d6)}

/* advice */
.advice-title{left:64px;top:844px;font-size:16px;font-weight:400;color:var(--blue)}
.quote{font-family:Georgia,serif;font-size:26px;line-height:1}
.q-open{left:60px;top:880px;color:var(--green)}
.q-close{left:370px;top:968px;color:var(--green)}
.advice-text{left:82px;width:200px;font-size:6.8px;line-height:8.6px;color:var(--text-grey)}
.a1{top:886px}.a2{top:930px}
.portrait{left:288px;top:880px;width:84px;height:84px;border-radius:50%;border:2px solid #ccc;background:linear-gradient(180deg,#c8c8c8,#8b8f95)}
.breeder{left:298px;top:976px;font-size:8px;color:#222}

/* eco card */
.eco-paper{left:423px;top:834px;width:228px;height:176px;background:#f4f4f4;transform:rotate(-2deg);box-shadow:0 2px 4px rgba(0,0,0,.3)}
.eco-green{left:432px;top:836px;width:210px;height:168px;background:var(--green);transform:rotate(1.5deg)}
.eco{left:428px;top:838px;width:218px;height:166px;background:#f7f7f7;border:5px solid var(--blue);text-align:center;color:#333}
.eco h3{font-family:"Dancing Script",cursive;font-weight:600;font-size:17px;color:var(--green-dark);margin-top:10px}
.eco p{font-size:6.6px;line-height:8.6px;width:176px;margin:6px auto 0}
.eco .more{position:absolute;right:10px;bottom:6px;font-size:7.5px;color:var(--blue);text-decoration:underline}

/* footer */
.footer{left:0;top:1032px;width:708px;height:168px;background:var(--grey-dark)}
.contact-panel{left:58px;top:1022px;width:236px;height:178px;background:linear-gradient(180deg,var(--board-1),var(--board-2))}
.panel-brand{left:92px;top:1042px;font-size:22px;color:var(--green-dark);display:flex;align-items:center;gap:6px}
.contact{left:94px;font-size:8.5px;color:var(--white);display:flex;align-items:center;gap:8px}
.contact svg{width:9px;height:9px}
.ct1{top:1077px}.ct2{top:1094px}.ct3{top:1110px}
.follow{left:464px;top:1054px;width:192px;height:26px;background:var(--grey-mid);color:var(--white);font-size:14px;line-height:26px;padding-left:10px}
.social{top:1052px;width:20px;height:24px;background:#2f6a9c;border:1px solid #aac}
.s1{left:578px}.s2{left:602px}.s3{left:626px}
.foot-links{right:55px;top:1097px;font-size:7.5px;color:var(--white)}
.copyright{right:55px;top:1111px;font-size:5.5px;color:#bbb}
</style>
</head>
<body>
<div class="page">

  <div class="abs hero-photo" role="img" aria-label="Wheat field with round hay bales under a golden sky"></div>
  <div class="abs nav-band"></div>
  <div class="abs brand"><span class="brand-dot"></span>Corvane</div>
  <nav class="abs nav">
    <a class="active" href="#">Home</a>
    <a class="item" href="#">About Us</a>
    <a class="item" href="#">Services</a>
    <a class="item" href="#">Contact Us</a>
  </nav>
  <div class="abs headline line-1"><span class="accent">M</span>ake Your</div>
  <div class="abs headline line-2"><span class="accent">Business</span> Flourise...</div>
  <div class="abs slider-dots"><span class="on"></span><span></span><span></span><span></span></div>

  <section class="abs about">
    <h2>About Us</h2>
    <p>Lorem Ipsum is simply dummy text of the printing and typesetting industry. Lorem Ipsum has been the industry's standard dummy text ever since the 1500s, when an unknown printer took a galley of type and scrambled it to make a type specimen book. It has survived not only five centuries, but also the leap into electronic typesetting, remaining essentially unchanged. It was popularised in the 1960s with the release of Letraset sheets containing Lorem Ipsum passages, and more recently with desktop publishing software like Aldus PageMaker including versions of Lorem Ipsum.</p>
  </section>
  <div class="abs about-photo" role="img" aria-label="Lone oak tree on a green meadow"></div>

  <article class="abs card c1">
    <div class="card-photo p1" role="img" aria-label="Young green seedling sprouting"></div>
    <h3>Research and development</h3><hr>
    <p>Lorem Ipsum is simply dummy text of the printing and typesetting industry. Lorem Ipsum has been the industry's standard dummy text ever since.</p>
    <span class="btn">read more</span>
  </article>
  <article class="abs card c2">
    <div class="card-photo p2" role="img" aria-label="Field split between green crop and bare soil under blue sky"></div>
    <h3>Fertilizers and Pesticides</h3><hr>
    <p>Lorem Ipsum is simply dummy text of the printing and typesetting industry. Lorem Ipsum has been the industry's standard dummy text ever since.</p>
    <span class="btn">read more</span>
  </article>
  <article class="abs card c3">
    <div class="card-photo p3" role="img" aria-label="Assorted fresh vegetables"></div>
    <h3>The Best Firming Product</h3><hr>
    <p>Lorem Ipsum is simply dummy text of the printing and typesetting industry. Lorem Ipsum has been the industry's standard dummy text ever since.</p>
    <span class="btn">read more</span>
  </article>

  <h2 class="abs advice-title">Advice from Breeder</h2>
  <div class="abs quote q-open">&ldquo;</div>
  <p class="abs advice-text a1">Lorem Ipsum is simply dummy text of the printing and typesetting industry. Lorem Ipsum has been the industry's standard dummy text ever since the 1500s.</p>
  <p class="abs advice-text a2">It has survived not only five centuries, but also the leap into electronic typesetting, remaining essentially unchanged. It was popularised in the 1960s with the release of Letraset sheets containing Lorem Ipsum passages, and more recently .</p>
  <div class="abs portrait" role="img" aria-label="Portrait of the breeder"></div>
  <div class="abs breeder">Breeder Name</div>
  <div class="abs quote q-close">&rdquo;</div>

  <div class="abs eco-paper"></div>
  <div class="abs eco-green"></div>
  <aside class="abs eco">
    <h3>Eco Frindly Technogy</h3>
    <p>Lorem Ipsum is simply dummy text of the printing and typesetting industry. Lorem Ipsum has been the industry's standard dummy text ever since.</p>
    <p style="margin-top:8px">It has survived not only five centuries, but also the leap into electronic typesetting, remaining essentially unchanged. It was popularised in the 1960s with the release of Letraset sheets containing Lorem Ipsum passages, and more recently .</p>
    <span class="more">Read More</span>
  </aside>

  <footer>
    <div class="abs footer"></div>
    <div class="abs contact-panel" role="img" aria-label="Wooden signboard standing in grass"></div>
    <div class="abs panel-brand"><span class="brand-dot"></span>Corvane</div>
    <div class="abs contact ct1">
      <svg viewBox="0 0 10 10"><path d="M5 0.5a3 3 0 0 1 3 3c0 2.2-3 6-3 6s-3-3.8-3-6a3 3 0 0 1 3-3z" fill="#fff"/><circle cx="5" cy="3.5" r="1.1" fill="#b8822a"/></svg>
      Address gose here</div>
    <div class="abs contact ct2">
      <svg viewBox="0 0 10 10"><path d="M2 1l2 2-1 1.2c.6 1.2 1.6 2.2 2.8 2.8L7 6l2 2-1.3 1.3C4.5 9 1 5.5.7 2.3z" fill="#fff"/></svg>
      Ph no: 0000000000/0000</div>
    <div class="abs contact ct3">
      <svg viewBox="0 0 10 10"><rect x="0.5" y="2" width="9" height="6.5" fill="#fff"/><path d="M0.5 2l4.5 3.5L9.5 2" stroke="#b8822a" stroke-width=".8" fill="none"/></svg>
      Email ID: hello@corvane.co.uk</div>

    <div class="abs follow">Follow us on</div>
    <div class="abs social s1" role="img" aria-label="Social profile"></div>
    <div class="abs social s2" role="img" aria-label="Social profile"></div>
    <div class="abs social s3" role="img" aria-label="Social profile"></div>
    <div class="abs foot-links">Home &nbsp;|&nbsp; About Us &nbsp;|&nbsp; Services &nbsp;|&nbsp; Contact Us</div>
    <div class="abs copyright">©2015-16 Corvane, All right reserved.</div>
  </footer>

</div>
</body>
</html>
```